Business Card Design for Pastor/Church Leadership - simple, elegant, "different"

Design a name card based on logo and color from our branding guide - see file "MBF Logo and Color".
The teal frame around the logo is not part of the logo and is a not necessary design element for the name card (as the attached PDF file may suggest).
The font suggested by branding is "Frutiger 55 Roman".
The file "not good.pdf", a sample of a name card that is NOT good.
- fonts too small to read
- the tagline on the logo "Still waters, open door" not easy to read with logo used in this design
- "MAPLE GROVE FELLOWSHIP" unnecessarily duplicated - possibly because logo too small
- not sure about the green frame, probably better to drop

Target Market(s)

broad, all people the pastor of an international church in Tokyo meets

Industry/Entity Type

Business

Contact Information for Business Card

Mattias R. Pellworth
Pastor
3-9-4 Kawaranodai, Shibuya-ku
Tokyo 150-0001 (Church)
2-21 Ochibamachi, Shibuya-ku
Tokyo 150-0035 (Home)
Tel: 03-5817-2963
E-mail: pastor@maplegrovefell.org
URL: http://www.maplegrovefell.org

Font styles to use
Sans Serif
Other font styles liked:
• Frutiger 55 Roman (want, not must)

Requirements
Must have
• must include logo
• must make use of the "bright turquoise color"
• Cyan = 59, Magenta = 0, Yellow=24, Black=0
• Red=3.1%, Green=91%, Blue=87.1%
• Key Info (name) must be easy to read (see notes on bad sample namecard attached)

```html
<!DOCTYPE html>
<html lang="en">
<head>
<meta charset="utf-8">
<title>Maple Grove Fellowship – Pastor Business Card</title>
<link href="https://fonts.googleapis.com/css2?family=Hind:wght@300;400&display=swap" rel="stylesheet">
<style>
  :root {
    --backdrop: #e9e6e1;
    --card: #fbfbfa;
    --turquoise: #4fc4c4;
    --turquoise-soft: #9fdcdc;
    --turquoise-wash: #dff2f2;
    --ink: #2a2a2a;
    --edge-dark: #1f1f1f;
  }
  * { margin: 0; padding: 0; box-sizing: border-box; }
  html, body {
    width: 1200px;
    height: 1022px;
    overflow: hidden;
    background: var(--backdrop);
    font-family: "Hind", "Helvetica Neue", Arial, sans-serif;
  }
  .business-card {
    position: absolute;
    left: 150px;
    top: 254px;
    width: 900px;
    height: 514px;
    background: var(--card);
    box-shadow: 0 18px 40px rgba(0,0,0,0.18);
    overflow: hidden;
  }
  .edge-strip {
    position: absolute;
    left: 0;
    width: 14px;
  }
  .edge-strip--dark { top: 250px; height: 40px; background: var(--edge-dark); }
  .edge-strip--accent { top: 290px; bottom: 0; background: var(--turquoise); }

  .logo-area {
    position: absolute;
    right: 60px;
    top: 40px;
    width: 380px;
    height: 270px;
    background: linear-gradient(135deg, var(--turquoise-wash), #eef8f8);
  }

  .identity {
    position: absolute;
    right: 60px;
    top: 330px;
    width: 380px;
    color: var(--turquoise);
  }
  .identity__name {
    display: flex;
    align-items: center;
    gap: 12px;
    font-size: 26px;
    font-weight: 400;
    letter-spacing: 1.5px;
    white-space: nowrap;
  }
  .identity__mark {
    width: 14px;
    height: 14px;
    flex: none;
    background: var(--turquoise);
  }
  .identity__rule {
    height: 2px;
    background: var(--turquoise);
    margin: 8px 0 6px;
  }
  .identity__tagline {
    font-size: 21px;
    font-weight: 300;
    letter-spacing: 0.5px;
    color: var(--turquoise-soft);
    padding-left: 26px;
  }

  .contact {
    position: absolute;
    left: 48px;
    top: 214px;
    color: var(--ink);
    font-size: 21px;
    line-height: 27px;
    font-weight: 400;
  }
  .contact__name {
    font-size: 31px;
    line-height: 36px;
    font-weight: 400;
    color: var(--turquoise);
  }
  .contact__role { margin-bottom: 16px; }
  .contact__address { margin-bottom: 14px; }
  .contact__label { color: var(--turquoise); }
  .contact__key {
    display: inline-block;
    width: 30px;
    color: var(--turquoise);
  }
</style>
</head>
<body>
  <main class="business-card">
    <div class="edge-strip edge-strip--dark"></div>
    <div class="edge-strip edge-strip--accent"></div>

    <div class="logo-area" role="img" aria-label="Large faint church logo mark"></div>

    <header class="identity">
      <div class="identity__name"><span class="identity__mark"></span>MAPLE GROVE FELLOWSHIP</div>
      <div class="identity__rule"></div>
      <div class="identity__tagline">Still waters, open door</div>
    </header>

    <section class="contact">
      <h1 class="contact__name">Mattias R. Pellworth</h1>
      <p class="contact__role">Pastor</p>
      <p class="contact__address">3-9-4 Kawaranodai, Shibuya-ku<br>Tokyo 150-0001 <span class="contact__label">(Church)</span></p>
      <p class="contact__address">2-21 Ochibamachi, Shibuya-ku<br>Tokyo 150-0035 <span class="contact__label">(Home)</span></p>
      <p><span class="contact__key">T:</span>03-5817-2963</p>
      <p><span class="contact__key">E:</span>pastor@maplegrovefell.org</p>
      <p><span class="contact__key">W:</span>www.maplegrovefell.org</p>
    </section>
  </main>
</body>
</html>
```